redesign laundry perfume webshop

We want to have a custom redesign for our website.
the focus should be luxury design . Please note that our "proefpakket" product is the most sold product.
Hello when desiging. please only use our product fotos, you can edit them, but dont make it look like there are other bottles etc.
Thank you for understanding.
Please dont show in english version (text). Use our language (dutch) use existing text on our website.
Also show our other pages as wel like category and product page etc.
Netherland and belgium
perfume
Coded - Design and coding required
5+ page
Designer to choose colors to be used in the design.

```html
<!DOCTYPE html>
<html lang="nl">
<head>
<meta charset="utf-8">
<title>Frissenza – Wasparfum</title>
<link href="https://fonts.googleapis.com/css2?family=Libre+Baskerville:wght@400;700&family=Lato:wght@400;700&family=Roboto:wght@400;700&display=swap" rel="stylesheet">
<style>
:root{
  --gold:#d9a92b;
  --gold-light:#ecc65a;
  --gold-dark:#b9861c;
  --ink:#2b2b2b;
  --text:#555;
  --muted:#8a8a8a;
  --light:#f3f3f3;
  --footer:#2d2d2d;
  --white:#fff;
  --quote:#1f3a6b;
}
*{box-sizing:border-box;margin:0;padding:0}
html,body{width:1200px;height:3276px;overflow:hidden;background:var(--white);font-family:"Lato",sans-serif;color:var(--text)}
.page{position:relative;width:1200px;height:3276px}

.topbar{height:43px;background:var(--light);display:flex;justify-content:center;align-items:center;gap:48px;font-size:12px;color:#666}
.topbar span{display:flex;align-items:center;gap:6px}

.header{position:relative;height:88px;background:var(--white)}
.brand{position:absolute;left:95px;top:-42px;width:130px;height:130px;border-radius:50%;background:var(--white);display:flex;flex-direction:column;align-items:center;justify-content:flex-end;padding-bottom:16px;gap:8px}
.brand .dot{width:44px;height:44px;border-radius:50%;background:var(--gold)}
.brand .name{font-family:"Libre Baskerville",serif;color:var(--gold);font-size:13px}
.search{position:absolute;left:309px;top:28px;width:368px;height:38px;border:1px solid #ddd;border-radius:19px;display:flex;align-items:center;padding:0 4px 0 20px;font-size:12px;color:#777;justify-content:space-between}
.search .go{width:30px;height:30px;border-radius:50%;background:var(--gold);display:flex;align-items:center;justify-content:center}
.tools{position:absolute;left:736px;top:30px;display:flex;align-items:center;gap:40px;font-size:12px;color:#444}
.tools .lang{display:flex;align-items:center;gap:8px}
.flag{width:32px;height:32px;border-radius:50%;background:linear-gradient(#c8202f 0 33%,#fff 33% 66%,#2a3f8f 66%)}
.tools span{display:flex;align-items:center;gap:8px}

.nav{height:46px;background:linear-gradient(var(--gold-light),var(--gold));display:flex;justify-content:center}
.nav a{color:var(--white);text-decoration:none;font-family:"Roboto",sans-serif;font-weight:700;font-size:14px;display:flex;align-items:center;padding:0 29px;border-right:1px solid rgba(255,255,255,.5)}
.nav a:last-child{border-right:0}

.hero{position:relative;height:556px;background:var(--light)}
.hero .curve{position:absolute;left:560px;top:520px;width:420px;height:120px;border-radius:50%;background:var(--white)}
.hero h1{position:absolute;left:178px;top:206px;font-family:"Libre Baskerville",serif;font-size:46px;color:var(--ink);font-weight:700}
.hero h2{position:absolute;left:178px;top:268px;font-size:36px;color:var(--ink);font-weight:400}
.btn{position:absolute;left:178px;top:322px;width:162px;height:42px;border-radius:21px;background:linear-gradient(var(--gold-light),var(--gold-dark));color:var(--white);font-size:13px;font-weight:700;display:flex;align-items:center;justify-content:center}
.arrow{position:absolute;top:265px;width:45px;height:45px;border-radius:50%;background:#111;display:flex;align-items:center;justify-content:center}
.hero-bottle{position:absolute;left:658px;top:55px;width:228px;height:534px;border-radius:30px 30px 10px 10px;background:linear-gradient(#fafafa 0 18%,#f3a522 18% 100%)}

.section-title{text-align:center;font-family:"Libre Baskerville",serif;font-weight:700;font-size:46px;color:var(--ink)}
.products{position:absolute;top:820px;left:0;width:1200px}
.grid{display:grid;grid-template-columns:repeat(3,309px);column-gap:24px;row-gap:29px;margin:29px 0 0 112px}
.card{position:relative;height:364px;background:var(--white);box-shadow:0 0 12px rgba(0,0,0,.08);border-radius:3px}
.card .img{position:absolute;left:102px;top:18px;width:105px;height:242px;border-radius:16px 16px 6px 6px}
.card .img.dropper{left:110px;width:92px;border-radius:10px 10px 20px 20px}
.card .title{position:absolute;left:23px;top:282px;font-family:"Libre Baskerville",serif;font-size:19px;color:var(--ink)}
.card .price{position:absolute;left:23px;top:317px;font-family:"Libre Baskerville",serif;font-size:18px;color:var(--ink)}
.card .cart{position:absolute;right:19px;top:288px;width:47px;height:47px;border-radius:3px;background:linear-gradient(var(--gold-light),var(--gold-dark));display:flex;align-items:center;justify-content:center}

.tasters{position:absolute;top:1770px;left:0;width:1200px;height:626px;background:var(--light);padding-top:74px}
.tasters .grid{margin-top:31px}
.tri{position:absolute;top:340px;width:0;height:0;border-top:12px solid transparent;border-bottom:12px solid transparent}

.reviews{position:absolute;top:2470px;left:0;width:1200px}
.divider{position:relative;width:714px;height:40px;margin:18px auto 0}
.divider:before{content:"";position:absolute;left:0;right:0;top:20px;height:2px;background:var(--gold)}
.divider .quote{position:absolute;left:327px;top:0;width:60px;height:40px;background:var(--white);text-align:center;font-family:"Libre Baskerville",serif;font-weight:700;font-size:76px;line-height:86px;color:var(--quote)}
.reviews p{width:710px;margin:22px auto 0;text-align:center;font-size:14px;line-height:26px;color:#666}
.reviews .who{text-align:center;font-size:19px;color:var(--ink);margin-top:16px}
.reviews .src{text-align:center;font-size:14px;color:#777;margin-top:8px}
.dots{display:flex;justify-content:center;gap:8px;margin-top:46px}
.dots i{width:12px;height:12px;border-radius:50%;background:#d6d6d6}
.dots i.on{background:var(--gold)}

.footer{position:absolute;top:2924px;left:0;width:1200px;height:352px;background:var(--footer);font-family:"Roboto",sans-serif;color:var(--white)}
.cols{display:flex;position:absolute;top:92px;left:110px}
.col{width:280px}
.col h3{font-size:22px;font-weight:700;margin-bottom:12px}
.col li{list-style:none;font-size:15px;line-height:26px;display:flex;align-items:center;gap:14px}
.social{display:flex;gap:8px}
.social i{width:33px;height:33px;background:var(--white)}
.copy{position:absolute;top:290px;width:1200px;text-align:center;font-size:14px}
</style>
</head>
<body>
<div class="page">
  <div class="topbar">
    <span><svg width="12" height="10" viewBox="0 0 12 10"><path d="M1 5l3 3 7-7" stroke="#d9a92b" stroke-width="2" fill="none"/></svg>Gratis verzending boven de €200!</span>
    <span><svg width="12" height="10" viewBox="0 0 12 10"><path d="M1 5l3 3 7-7" stroke="#d9a92b" stroke-width="2" fill="none"/></svg>Lage prijzen!</span>
  </div>

  <header class="header">
    <div class="brand"><span class="dot"></span><span class="name">FRISSENZA</span></div>
    <div class="search">Zoek naar iets<span class="go"><svg width="12" height="12" viewBox="0 0 12 12"><circle cx="5" cy="5" r="3.5" stroke="#fff" stroke-width="1.6" fill="none"/><path d="M8 8l3 3" stroke="#fff" stroke-width="1.6"/></svg></span></div>
    <div class="tools">
      <div class="lang"><span class="flag"></span>Dutch ⌄</div>
      <span><svg width="11" height="12" viewBox="0 0 11 12"><circle cx="5.5" cy="3" r="3" fill="#444"/><path d="M0 12c0-4 11-4 11 0z" fill="#444"/></svg>Mijn rekening</span>
      <span><svg width="13" height="11" viewBox="0 0 13 11"><path d="M0 1h2l2 6h7l2-5H3" stroke="#444" stroke-width="1.6" fill="none"/><circle cx="5" cy="9.5" r="1.3" fill="#444"/><circle cx="10" cy="9.5" r="1.3" fill="#444"/></svg>: 0.00</span>
    </div>
  </header>

  <nav class="nav"><a>THUIS</a><a>OVER ONS</a><a>TOP VERKOPER</a><a>PRODUCT</a><a>BLOGGEN</a><a>CONTACT</a></nav>

  <section class="hero">
    <div class="curve"></div>
    <h1>FRISSENZA</h1>
    <h2>WASPARFUM BEDRIJF</h2>
    <div class="btn">BEGIN</div>
    <div class="arrow" style="left:68px"><svg width="10" height="14" viewBox="0 0 10 14"><path d="M7 2L2 7l5 5" stroke="#fff" stroke-width="2" fill="none"/></svg></div>
    <div class="arrow" style="left:1087px"><svg width="10" height="14" viewBox="0 0 10 14"><path d="M3 2l5 5-5 5" stroke="#fff" stroke-width="2" fill="none"/></svg></div>
    <div class="hero-bottle" role="img" aria-label="Productfoto: fles wasparfum Amberveld met oranje patroon"></div>
  </section>

  <section class="products">
    <h2 class="section-title">ONZE PRODUCTEN</h2>
    <div class="grid">
      <div class="card"><div class="img" role="img" aria-label="Productfoto fles Zijdezacht" style="background:linear-gradient(#f6f6f6 0 20%,#a9cdee 20%)"></div><div class="title">ZIJDEZACHT</div><div class="price">14.95</div><div class="cart"><svg width="18" height="15" viewBox="0 0 13 11"><path d="M0 1h2l2 6h7l2-5H3" stroke="#fff" stroke-width="1.6" fill="none"/><circle cx="5" cy="9.5" r="1.3" fill="#fff"/><circle cx="10" cy="9.5" r="1.3" fill="#fff"/></svg></div></div>
      <div class="card"><div class="img" role="img" aria-label="Productfoto fles Azuurgaard" style="background:linear-gradient(#f6f6f6 0 20%,#7fb3e3 20%)"></div><div class="title">AZUURGAARD</div><div class="price">14.95</div><div class="cart"><svg width="18" height="15" viewBox="0 0 13 11"><path d="M0 1h2l2 6h7l2-5H3" stroke="#fff" stroke-width="1.6" fill="none"/><circle cx="5" cy="9.5" r="1.3" fill="#fff"/><circle cx="10" cy="9.5" r="1.3" fill="#fff"/></svg></div></div>
      <div class="card"><div class="img" role="img" aria-label="Productfoto fles Amberveld" style="background:linear-gradient(#f6f6f6 0 20%,#f3a522 20%)"></div><div class="title">AMBERVELD</div><div class="price">14.95</div><div class="cart"><svg width="18" height="15" viewBox="0 0 13 11"><path d="M0 1h2l2 6h7l2-5H3" stroke="#fff" stroke-width="1.6" fill="none"/><circle cx="5" cy="9.5" r="1.3" fill="#fff"/><circle cx="10" cy="9.5" r="1.3" fill="#fff"/></svg></div></div>
      <div class="card"><div class="img" role="img" aria-label="Productfoto fles Rozenhof" style="background:linear-gradient(#f6f6f6 0 20%,#c92a32 20%)"></div><div class="title">ROZENHOF</div><div class="price">14.95</div><div class="cart"><svg width="18" height="15" viewBox="0 0 13 11"><path d="M0 1h2l2 6h7l2-5H3" stroke="#fff" stroke-width="1.6" fill="none"/><circle cx="5" cy="9.5" r="1.3" fill="#fff"/><circle cx="10" cy="9.5" r="1.3" fill="#fff"/></svg></div></div>
      <div class="card"><div class="img" role="img" aria-label="Productfoto fles Indigotij" style="background:linear-gradient(#f6f6f6 0 20%,#2c2f7a 20%)"></div><div class="title">INDIGOTIJ</div><div class="price">14.95</div><div class="cart"><svg width="18" height="15" viewBox="0 0 13 11"><path d="M0 1h2l2 6h7l2-5H3" stroke="#fff" stroke-width="1.6" fill="none"/><circle cx="5" cy="9.5" r="1.3" fill="#fff"/><circle cx="10" cy="9.5" r="1.3" fill="#fff"/></svg></div></div>
      <div class="card"><div class="img dropper" role="img" aria-label="Productfoto proefflesje Azuurgaard" style="background:linear-gradient(#f6f6f6 0 25%,#5a2c10 25% 50%,#f8f5ec 50%)"></div><div class="title">AZUURGAARD</div><div class="price">14.95</div><div class="cart"><svg width="18" height="15" viewBox="0 0 13 11"><path d="M0 1h2l2 6h7l2-5H3" stroke="#fff" stroke-width="1.6" fill="none"/><circle cx="5" cy="9.5" r="1.3" fill="#fff"/><circle cx="10" cy="9.5" r="1.3" fill="#fff"/></svg></div></div>
    </div>
  </section>

  <section class="tasters">
    <h2 class="section-title">PROEFPAKKET</h2>
    <div class="tri" style="left:44px;border-right:22px solid #aaa"></div>
    <div class="tri" style="left:1134px;border-left:22px solid var(--gold)"></div>
    <div class="grid">
      <div class="card"><div class="img dropper" role="img" aria-label="Productfoto proefflesje Indigotij" style="background:linear-gradient(#f6f6f6 0 25%,#5a2c10 25% 50%,#f8f5ec 50%)"></div><div class="title">INDIGOTIJ</div><div class="price">14.95</div><div class="cart"><svg width="18" height="15" viewBox="0 0 13 11"><path d="M0 1h2l2 6h7l2-5H3" stroke="#fff" stroke-width="1.6" fill="none"/><circle cx="5" cy="9.5" r="1.3" fill="#fff"/><circle cx="10" cy="9.5" r="1.3" fill="#fff"/></svg></div></div>
      <div class="card"><div class="img dropper" role="img" aria-label="Productfoto proefflesje Amberveld" style="background:linear-gradient(#f6f6f6 0 25%,#5a2c10 25% 50%,#f8f5ec 50%)"></div><div class="title">AMBERVELD</div><div class="price">14.95</div><div class="cart"><svg width="18" height="15" viewBox="0 0 13 11"><path d="M0 1h2l2 6h7l2-5H3" stroke="#fff" stroke-width="1.6" fill="none"/><circle cx="5" cy="9.5" r="1.3" fill="#fff"/><circle cx="10" cy="9.5" r="1.3" fill="#fff"/></svg></div></div>
      <div class="card"><div class="img dropper" role="img" aria-label="Productfoto proefflesje Zijdezacht" style="background:linear-gradient(#f6f6f6 0 25%,#5a2c10 25% 50%,#f8f5ec 50%)"></div><div class="title">ZIJDEZACHT</div><div class="price">14.95</div><div class="cart"><svg width="18" height="15" viewBox="0 0 13 11"><path d="M0 1h2l2 6h7l2-5H3" stroke="#fff" stroke-width="1.6" fill="none"/><circle cx="5" cy="9.5" r="1.3" fill="#fff"/><circle cx="10" cy="9.5" r="1.3" fill="#fff"/></svg></div></div>
    </div>
  </section>

  <section class="reviews">
    <h2 class="section-title">GETUIGENISSEN</h2>
    <div class="divider"><span class="quote">“</span></div>
    <p>Wat ben ik gelukkig met deze geurtjes! Mijn vriend en ik zijn heel gevoelig als het op geur aankomt. Wij worden snel onpasselijk van luchtjes, maar als het de juiste zijn worden wij heel blij. Wat ben ik blij dat ik jullie ontdekt heb. Ik ben nog met het proefpakket bezig, maar ik weet nu al dat ik dit voortaan ga gebruiken.<br>Echt zo lekker!</p>
    <div class="who">Lotte Vermeer</div>
    <div class="src">Klant ervaring online</div>
    <div class="dots"><i></i><i class="on"></i><i></i><i></i></div>
  </section>

  <footer class="footer">
    <div class="cols">
      <div class="col"><h3>Menu</h3><ul><li>»&nbsp; Thuis</li><li>»&nbsp; Product</li><li>»&nbsp; Contact</li></ul></div>
      <div class="col"><h3>INFORMATIE</h3><ul><li>»&nbsp; Over ons</li><li>»&nbsp; FAQ</li><li>»&nbsp; Recensies</li><li>»&nbsp; Bloggen</li></ul></div>
      <div class="col"><h3>CONTACT</h3><ul>
        <li><svg width="10" height="13" viewBox="0 0 10 13"><path d="M5 13C1 8 0 6 0 5a5 5 0 0110 0c0 1-1 3-5 8z" fill="#d9a92b"/><circle cx="5" cy="5" r="1.8" fill="#2d2d2d"/></svg>123,Lorem ipsum dolor sit</li>
        <li><svg width="12" height="12" viewBox="0 0 12 12"><path d="M2 0l2.5 3-1.5 1.5a8 8 0 004.5 4.5L9 7.5l3 2.5-2 2C5 12 0 7 0 2z" fill="#d9a92b"/></svg>+31201234567</li>
        <li><svg width="13" height="10" viewBox="0 0 13 10"><rect width="13" height="10" fill="#d9a92b"/><path d="M0 0l6.5 5L13 0" stroke="#2d2d2d" fill="none"/></svg>info@frissenza.nl</li>
      </ul></div>
      <div class="col"><h3>VOLG ONS</h3><div class="social" aria-label="Sociale media"><i></i><i></i><i></i><i></i></div></div>
    </div>
    <div class="copy">© Copyrights Frissenza 2023. Alle rechten voorbehouden</div>
  </footer>
</div>
</body>
</html>
```